Business Card Design and Basic Text Logo

We are looking for a business card design for an e-business company. Our business is the parent company of a few website businesses. The final logo and business card design will communicate a conservative but modern and expansive business

The Logo text is: 87Merchant
We would also like a basic text logo design for 87Merchant. The logo could also fill up the reverse side of the business card.

The colours we would like to use are:
White
Navy
Black

This is the text that will be added to the card:

Dean Colley
Business Development Manager

Phone: +61 417 658 294
Email: dean.colley@87merchant.com.au

Industry/Entity Type

Business

Logo Text

87Merchant

Logo styles of interest
Pictorial/Combination Logo
Requirements
Must have
• Modern and attractive design
Nice to have
• communicate a conservative but modern and expansive business
Should not have
• Should be too dull and plan
• But also should be overly colourful

```html
<!DOCTYPE html>
<html lang="en">
<head>
<meta charset="utf-8">
<title>87Merchant Business Card</title>
<link rel="stylesheet" href="https://fonts.googleapis.com/css2?family=Open+Sans:ital,wght@0,400;0,600;0,700;1,400&display=swap">
<style>
  :root {
    --page: #ffffff;
    --card: #ffffff;
    --card-edge: #1a1a1a;
    --ink: #1c1c1c;
    --navy: #27348b;
  }
  html, body {
    margin: 0;
    padding: 0;
    width: 1200px;
    height: 1000px;
    overflow: hidden;
    background: var(--page);
    font-family: "Open Sans", Arial, sans-serif;
  }
  .canvas {
    position: relative;
    width: 1200px;
    height: 1000px;
  }
  .card {
    position: absolute;
    top: 376px;
    width: 469px;
    height: 264px;
    background: var(--card);
    border: 1px solid var(--card-edge);
    box-sizing: content-box;
  }
  .card--front { left: 61px; }
  .card--back { left: 667px; }

  .brand {
    position: absolute;
    display: flex;
    align-items: center;
    white-space: nowrap;
  }
  .brand__mark {
    flex: none;
    background: var(--navy);
  }
  .brand__name {
    margin: 0;
    font-weight: 700;
    color: var(--ink);
    line-height: 1;
  }

  .card--front .brand {
    left: 56px;
    top: 110px;
    gap: 12px;
  }
  .card--front .brand__mark {
    width: 38px;
    height: 38px;
  }
  .card--front .brand__name {
    font-size: 52px;
  }

  .card--back .brand {
    left: 133px;
    top: 91px;
    gap: 7px;
  }
  .card--back .brand__mark {
    width: 22px;
    height: 22px;
  }
  .card--back .brand__name {
    font-size: 29px;
  }

  .contact {
    position: absolute;
    left: 133px;
    top: 160px;
    color: var(--ink);
  }
  .contact__name {
    margin: 0;
    font-size: 15px;
    font-weight: 700;
    line-height: 20px;
  }
  .contact__role {
    margin: 0;
    font-size: 13.4px;
    font-style: italic;
    line-height: 16px;
    letter-spacing: 0.3px;
  }
</style>
</head>
<body>
  <main class="canvas">
    <section class="card card--front" aria-label="Card front">
      <div class="brand">
        <span class="brand__mark" aria-hidden="true"></span>
        <p class="brand__name">87Merchant</p>
      </div>
    </section>

    <section class="card card--back" aria-label="Card back">
      <div class="brand">
        <span class="brand__mark" aria-hidden="true"></span>
        <p class="brand__name">87Merchant</p>
      </div>
      <div class="contact">
        <p class="contact__name">Dean Colley</p>
        <p class="contact__role">Business Development Manager</p>
      </div>
    </section>
  </main>
</body>
</html>
```